Harwick DCS Informational Flyer

We need a visually-appealing informational 1-page (Letter paper, 8.5 by 11.0 inches, portrait orientation) handout to promote academic and research programs of Harwick University Department of Digital and Computing Studies. This handout will be sent to other universities to recruit students and used and job/career fairs to promote the computing programs at Harwick.

Target Market(s)

Prospective graduate students in computing (both in US and international)

Industry/Entity Type

Education

Requirements
Must have
• (1) Incorporate (most of) the department information in a visually appealing way
• (2) Follow Harwick Brand Guidelines: https://identity.harwickuni.edu/brand-guidelines
Nice to have
• Background pictures of Philadelphia, Harwick University, and/or NAVL building (http://sdp.harwickuni.edu/research/NAVL)

```html
<!DOCTYPE html>
<html lang="en">
<head>
<meta charset="utf-8">
<title>Harwick DCS Informational Flyer</title>
<link href="https://fonts.googleapis.com/css2?family=Fira+Sans:wght@400;600;700&display=swap" rel="stylesheet">
<style>
:root{
  --cherry:#a21c38;
  --cherry-dark:#9a1a34;
  --ink:#111;
  --text:#222;
  --rule:#c8c8c8;
  --bullet-red:#e0202e;
  --bullet-grey:#8a8a8a;
  --paper:#fff;
}
*{margin:0;padding:0;box-sizing:border-box}
html,body{width:939px;height:1200px;overflow:hidden;background:var(--paper)}
body{font-family:"Fira Sans",sans-serif;color:var(--text);position:relative}
.abs{position:absolute}

.brand{left:58px;top:70px;display:flex;align-items:center;gap:16px}
.brand-square{width:76px;height:84px;background:var(--cherry)}
.brand-name{font-weight:700;font-size:44px;line-height:1;color:var(--ink);letter-spacing:1px}

.contact{right:66px;top:60px;text-align:right;color:var(--ink)}
.contact .phone{font-weight:700;font-size:24px;line-height:30px}
.contact .web{font-weight:600;font-size:17px;line-height:26px}
.contact .addr{font-size:14px;line-height:19px;margin-top:8px}

.about-band{left:14px;top:193px;width:911px;height:237px;background:var(--cherry);color:#fff;padding:20px 44px 0 44px}
.about-band h1{font-weight:700;font-size:29px;letter-spacing:.2px;line-height:36px}
.about-band h2{font-weight:600;font-size:21px;margin-top:18px;line-height:28px}
.about-band p{font-size:13.2px;line-height:18.9px;margin-top:9px;text-align:justify}

.facts-title{left:58px;top:436px;font-weight:700;font-size:43px;color:var(--ink);letter-spacing:-.3px}

.section-head{font-weight:600;font-size:20px;color:var(--cherry);line-height:26px}
.sub-note{font-size:13px;color:var(--cherry)}
ul{list-style:none}
.dots li{position:relative;padding-left:21px;font-size:13px;line-height:17.5px;margin-bottom:2.8px;color:var(--text)}
.dots li::before{content:"";position:absolute;left:0;top:4px;width:10px;height:10px;border-radius:50%;background:var(--bullet-red)}
.subdots li{position:relative;padding-left:15px;font-size:13px;line-height:17.5px;color:var(--text)}
.subdots li::before{content:"";position:absolute;left:2px;top:6px;width:7px;height:7px;border-radius:50%;background:var(--bullet-grey)}

.col-divider{left:397px;top:528px;width:1px;height:370px;background:var(--rule)}
.rule-left{left:58px;top:682px;width:340px;height:1px;background:var(--rule)}
.rule-right{left:398px;top:650px;width:484px;height:1px;background:var(--rule)}

.people{left:59px;top:520px;width:330px}
.degrees{left:59px;top:699px;width:330px}
.rankings{left:425px;top:520px;width:470px}
.rank-grid{display:grid;grid-template-columns:257px 200px;margin-top:10px}
.research{left:425px;top:667px;width:460px}
.research .subdots{margin:2px 0 0 21px}

.photo{top:920px;height:188px}
.photo-campus{left:14px;width:349px;background:linear-gradient(160deg,#8a7a3a,#5b5240 45%,#3e3a36)}
.photo-city{left:370px;width:258px;background:linear-gradient(180deg,#c9d0d4,#8f9492 45%,#5d6a52)}
.photo-students{left:635px;width:289px;background:linear-gradient(150deg,#c52a3c,#8e2030 55%,#5a1a22)}

.footer-strip{left:14px;top:1108px;width:911px;height:5px;background:#111}
.footer{left:14px;top:1113px;width:911px;height:73px;background:var(--cherry-dark);color:#fff;display:flex;justify-content:space-between;align-items:center;gap:24px;padding:0 44px 10px 44px;white-space:nowrap}
.footer .link{font-weight:600;font-size:18px}
.footer .mail{font-size:18px}
.footer .mail b{font-weight:600}
</style>
</head>
<body>

<div class="abs brand">
  <div class="brand-square"></div>
  <div class="brand-name">HARWICK UNIVERSITY</div>
</div>

<div class="abs contact">
  <div class="phone">(555) 014-2290</div>
  <div class="web">http://dcs.harwickuni.edu</div>
  <div class="addr">420 Alder Row<br>Philadelphia, PA 19000 USA</div>
</div>

<section class="abs about-band">
  <h1>DEPARTMENT OF DIGITAL AND COMPUTING STUDIES</h1>
  <h2>About Harwick University</h2>
  <p>Harwick University is an R1 (highest research activity) institution that ranks among the top 55 among public colleges and universities in the National College Review ranking. Serving more than 38,000 students, Harwick is the 26th largest university and 6th largest provider of graduate school education in the United States. Located in the heart of Philadelphia, Harwick offers students opportunities to explore the 5th largest city in U.S., known for its arts, culture and history, and affordable living. In addition, Harwick University is in close proximity to many companies specializing in information technology, health care, biotechnology, and finance.</p>
</section>

<h2 class="abs facts-title">Harwick DCS Department Facts</h2>

<div class="abs col-divider"></div>
<div class="abs rule-left"></div>
<div class="abs rule-right"></div>

<section class="abs people">
  <h3 class="section-head">PEOPLE</h3>
  <ul class="dots" style="margin-top:8px">
    <li>&gt;60 faculty members</li>
    <li>&gt;1000 undergraduate students</li>
    <li>&gt;100 graduate students</li>
    <li>Harwick DCS alums work at companies such as Zenlo, Pinecast, KV, Searcho, NTX, RK Bristow, Linkwise, Quillsoft, Datavane</li>
  </ul>
</section>

<section class="abs degrees">
  <h3 class="section-head">DEGREE PROGRAMS</h3>
  <ul class="dots" style="margin-top:8px">
    <li>B.A. and B.S. in Computer Science (CS)</li>
    <li>B.A. and B.S. in Information Science and Technology (IS&amp;T)</li>
    <li>PSM in Cyber Defense and Information Assurance</li>
    <li>M.S. in Computer Science</li>
    <li>M.S. in Computational Data Science</li>
    <li>M.S. in Information Science and Technology</li>
    <li>Ph.D. in Digital and Computing Studies</li>
  </ul>
</section>

<section class="abs rankings">
  <h3 class="section-head">DEPARTMENT RANKINGS</h3>
  <div class="sub-note">(according to http://deptindex.example.org )</div>
  <div class="rank-grid">
    <ul class="dots">
      <li>70 th overall in US CS departments</li>
      <li>22 nd in computer vision</li>
      <li>35 th in operating systems</li>
    </ul>
    <ul class="dots">
      <li>16 th in computer networks</li>
      <li>34 th in artificial intelligence</li>
    </ul>
  </div>
</section>

<section class="abs research">
  <h3 class="section-head">RESEARCH</h3>
  <ul class="dots" style="margin-top:8px">
    <li>Over $3 million in annual external research funding from sources such as federal science, health and defense agencies, the Commonwealth of Pennsylvania, and industry</li>
    <li>Research focus areas:</li>
  </ul>
  <ul class="subdots">
    <li>Artificial Intelligence</li>
    <li>Computer Vision</li>
    <li>Data Mining and Machine Learning</li>
    <li>Information Security and Forensics</li>
    <li>Operating and Distributed Systems</li>
    <li>Web Data Management</li>
    <li>Wireless Networks and Mobile Computing</li>
  </ul>
</section>

<div class="abs photo photo-campus" role="img" aria-label="Photo of students walking along a tree-lined campus path in autumn"></div>
<div class="abs photo photo-city" role="img" aria-label="Photo of the Philadelphia skyline above a busy avenue"></div>
<div class="abs photo photo-students" role="img" aria-label="Photo of smiling students in cherry university shirts at a campus event"></div>

<div class="abs footer-strip"></div>
<footer class="abs footer">
  <span class="link">http://dcs.harwickuni.edu/GradAdmissions</span>
  <span class="mail">email: <b>dcsadmissions@harwickuni.edu</b></span>
</footer>

</body>
</html>
```